ZRD Roofing Billboard Design

Looking for a fresh new billboard design with my new headshot photo and using some info from my previous billboard and maybe website for design/content inspiration. My website is https://zrdroofing.com/

Also attached are my logo and current lawn sign design. I am looking for something simple, clean and modern. The landing page website should be 3816tops.com like my previous billboard has.

```html
<!DOCTYPE html>
<html lang="en">
<head>
<meta charset="UTF-8">
<title>ZRD Roofing Billboard</title>
<link rel="stylesheet" href="https://fonts.googleapis.com/css2?family=Bebas+Neue&family=Montserrat:wght@700;800&display=swap">
<style>
  :root {
    --page-bg: #e9eef4;
    --navy-dark: #08193b;
    --navy-mid: #0a3566;
    --navy-light: #0d4b87;
    --accent-green: #5cb85c;
    --white: #ffffff;
    --ink: #0c1a3c;
    --photo-top: #7d8896;
    --photo-bottom: #b9c6dc;
  }
  * { margin: 0; padding: 0; box-sizing: border-box; }
  html, body {
    width: 1200px; height: 580px; overflow: hidden;
    background: var(--page-bg);
  }
  .billboard {
    position: absolute; left: 20px; top: 121px;
    width: 1160px; height: 337px;
    overflow: hidden;
    background: var(--white);
  }
  .headline-panel {
    position: absolute; left: 0; top: 0;
    width: 1160px; height: 225px;
    background: linear-gradient(90deg, var(--navy-dark) 0%, var(--navy-mid) 50%, var(--navy-light) 100%);
  }
  .accent-rule {
    position: absolute; left: 0; top: 225px;
    width: 800px; height: 3px;
    background: var(--accent-green);
  }
  .brand {
    position: absolute; left: 61px; top: 28px;
    width: 200px; text-align: center;
  }
  .brand-mark {
    width: 144px; height: 144px; margin: 0 auto;
    border-radius: 50%;
    background: var(--white);
    border: 4px solid var(--accent-green);
  }
  .brand-name {
    margin-top: 12px;
    font-family: "Montserrat", sans-serif;
    font-weight: 800; font-size: 17px;
    color: var(--white); white-space: nowrap;
  }
  .headline {
    font-family: "Bebas Neue", sans-serif;
    color: var(--white); position: absolute;
    line-height: 1; white-space: nowrap;
  }
  .headline-your {
    left: 308px; top: 47px; width: 134px; height: 39px;
    background: var(--white); color: var(--ink);
    font-size: 48px; text-align: center; line-height: 44px;
    clip-path: polygon(4% 0, 100% 0, 96% 100%, 0 100%);
  }
  .headline-trusted { left: 307px; top: 88px; font-size: 48px; }
  .headline-roofer { left: 452px; top: 36px; font-size: 117px; letter-spacing: 1px; }
  .headline-place { left: 306px; top: 133px; font-size: 74px; letter-spacing: 1px; }
  .contact {
    position: absolute; left: 57px; top: 236px;
    display: flex; align-items: center; gap: 10px;
  }
  .phone-icon { width: 76px; height: 76px; }
  .phone-number {
    font-family: "Montserrat", sans-serif;
    font-weight: 800; font-size: 74px;
    color: var(--ink); line-height: 1; white-space: nowrap;
  }
  .headshot {
    position: absolute; left: 808px; top: 45px;
    width: 352px; height: 292px;
    background: linear-gradient(180deg, var(--photo-top) 0%, var(--photo-bottom) 100%);
  }
</style>
</head>
<body>
  <main class="billboard">
    <section class="headline-panel">
      <div class="brand">
        <div class="brand-mark"></div>
        <p class="brand-name">ZRD ROOFING LCC</p>
      </div>
      <h1>
        <span class="headline headline-your">YOUR</span>
        <span class="headline headline-trusted">TRUSTED</span>
        <span class="headline headline-roofer">ROOFER</span>
        <span class="headline headline-place">IN NEWINGTON, CT</span>
      </h1>
    </section>
    <div class="accent-rule"></div>
    <div class="contact">
      <svg class="phone-icon" viewBox="0 0 76 76" aria-hidden="true">
        <path fill="#0c1a3c" d="M14 8c3-2 6-2 8 1l8 12c2 3 1 6-1 8l-4 3c3 7 9 14 16 18l4-3c2-2 5-2 7 0l10 9c2 2 2 5 0 7l-5 5c-4 4-11 4-18-1C26 58 15 45 9 31 5 21 6 14 14 8z"/>
        <path fill="none" stroke="#0c1a3c" stroke-width="5" stroke-linecap="round" d="M40 20a16 16 0 0 1 16 16M42 8a28 28 0 0 1 28 28"/>
      </svg>
      <p class="phone-number">(860) 555-0142</p>
    </div>
    <div class="headshot" role="img" aria-label="Headshot of the company owner, smiling, in a light blue shirt in front of a grey tiled roof"></div>
  </main>
</body>
</html>
```